Business Card Design for a Jockey's Agent

A business card design that helps to develop a brand or identity for myself, the agent, perhaps on one side with a clean minimalist design, and on the other side a simple design with the two jockeys names i currently represent. Those jockeys may change twice a year as they move around the country, switch agents, etc, so i think keeping one side designed to promote the agent and a second side that can be changed easily to identify the jockeys i currently represent would be the best.

Target Market(s)

Thoroughbred racehorse trainers

Industry/Entity Type

Business

Contact Information for Business Card

Gareth Lindqvist - Jockey Agent
mobile (555) 813 2649
garethklindqvist2fenmail.com

Jockeys: Tobias Wren, Marlow Pendry

Font styles to use
Serif

Requirements
Must have
• contact info and modern feel and font
Nice to have
• clean minimalist element of racing, jockey silk, helmut or crop, finish marker pole from racetrack etc,
Should not have
• DONT HAVE ANY KIND OF LOGO ETC. IMAGE IS ONE OF MY RACEHORSES TO HELP FINISH BRIEF.
• racing horse, stuffy vintage racing feel or Weekly Paddock Sheet fonts

```html
<!DOCTYPE html>
<html lang="en">
<head>
<meta charset="utf-8">
<title>Gareth Lindqvist – Jockey Agent Business Card</title>
<link rel="stylesheet" href="https://fonts.googleapis.com/css2?family=Cinzel:wght@400&family=Crimson+Pro:wght@400&family=Open+Sans:wght@400;600&display=swap">
<style>
  :root {
    --ink: #000000;
    --paper: #ffffff;
    --backdrop: #e7e3dd;
    --silhouette-light: #e9e9e9;
    --silhouette-mid: #a9a9a9;
    --rule-grey: #2a2a2a;
  }
  * { margin: 0; padding: 0; box-sizing: border-box; }
  html, body {
    width: 1200px; height: 912px; overflow: hidden;
    background: var(--backdrop);
  }
  .canvas { position: relative; width: 1200px; height: 912px; }

  .card {
    position: absolute; top: 306px;
    width: 495px; height: 299px;
    box-shadow: 0 6px 18px rgba(0,0,0,0.18);
    overflow: hidden;
  }

  /* Back side */
  .card--back { left: 85px; background: var(--ink); }
  .card--back .racing-art {
    position: absolute; left: 180px; top: 104px;
    width: 134px; height: 76px;
    border-radius: 40% 50% 30% 45%;
    background: linear-gradient(90deg, var(--silhouette-mid), var(--silhouette-light));
  }

  /* Front side */
  .card--front { left: 620px; background: var(--paper); }
  .header-band {
    position: absolute; left: 0; top: 0; width: 100%; height: 106px;
    background: var(--ink);
  }
  .header-band::after {
    content: ""; position: absolute; left: 0; right: 0; top: 97px;
    height: 3px; background: var(--paper);
  }
  .header-art {
    position: absolute; left: 4px; top: 24px; width: 156px; height: 74px;
    border-radius: 45% 50% 0 0;
    background: linear-gradient(90deg, var(--silhouette-light), var(--silhouette-mid));
  }
  .agent-name {
    position: absolute; left: 136px; top: 11px; width: 253px;
    border-top: 2px solid var(--paper); border-bottom: 2px solid var(--paper);
    color: var(--paper);
    font-family: "Cinzel", serif; font-size: 25px; line-height: 32px;
    text-align: center; letter-spacing: 0.2px; white-space: nowrap;
  }
  .agent-title {
    position: absolute; left: 136px; top: 51px; width: 253px;
    color: var(--paper);
    font-family: "Open Sans", sans-serif; font-size: 18px;
    text-align: center;
  }

  .roster-label {
    position: absolute; left: 83px; top: 152px;
    font-family: "Open Sans", sans-serif; font-weight: 600; font-size: 16px;
  }
  .roster { position: absolute; left: 27px; top: 189px; list-style: none; }
  .roster li { display: flex; height: 26px; align-items: baseline; }
  .jockey-name {
    width: 166px;
    font-family: "Crimson Pro", serif; font-size: 22px;
  }
  .jockey-weight {
    font-family: "Crimson Pro", serif; font-size: 16px;
  }
  .divider {
    position: absolute; left: 251px; top: 137px; width: 1px; height: 139px;
    background: var(--rule-grey);
  }
  .contact { position: absolute; left: 275px; top: 176px; list-style: none; }
  .contact li {
    display: flex; align-items: center; height: 26px;
    font-family: "Open Sans", sans-serif; font-size: 13px;
  }
  .contact svg { width: 18px; height: 18px; margin-right: 6px; flex: none; }
</style>
</head>
<body>
<main class="canvas">
  <section class="card card--back" aria-label="Card back">
    <div class="racing-art" role="img" aria-label="Silhouette of two jockeys racing on horseback"></div>
  </section>

  <section class="card card--front" aria-label="Card front">
    <header class="header-band">
      <div class="header-art" role="img" aria-label="Silhouette of jockeys on racehorses, head-on view"></div>
      <h1 class="agent-name">Gareth Lindqvist</h1>
      <p class="agent-title">Jockey Agent</p>
    </header>

    <p class="roster-label">Jockeys:</p>
    <ul class="roster">
      <li><span class="jockey-name">Tobias Wren</span><span class="jockey-weight">112 lbs</span></li>
      <li><span class="jockey-name">Marlow Pendry</span><span class="jockey-weight">114 lbs</span></li>
    </ul>

    <div class="divider"></div>

    <ul class="contact">
      <li>
        <svg viewBox="0 0 20 20" aria-hidden="true">
          <circle cx="10" cy="10" r="8.5" fill="none" stroke="#000" stroke-width="1.5"/>
          <path d="M7 5.5 L8.6 7.6 L7.8 8.8 Q9 11.3 11.2 12.2 L12.4 11.4 L14.5 13 L13.4 14.6 Q8.5 14.5 5.6 7 Z" fill="#000"/>
        </svg>
        (555) 813 2649
      </li>
      <li>
        <svg viewBox="0 0 20 20" aria-hidden="true">
          <rect x="2" y="5" width="16" height="11" fill="none" stroke="#000" stroke-width="1.5"/>
          <path d="M2 5 L10 11 L18 5 M2 16 L8 10 M18 16 L12 10" fill="none" stroke="#000" stroke-width="1.5"/>
        </svg>
        garethklindqvist2fenmail.com
      </li>
    </ul>
  </section>
</main>
</body>
</html>
```